Real Estate Listing Signs for standard Yard arms

I need real estate listing signs done, for the standard sized sign to be hung beneath a white yard arm. To match existing logo. Information to be included:
-Logo
-Business name
-Phone number
-Marden Fosk Tundra Circle & Marden Fosk realty logos (smaller print)

Colors to be Red and anywhere in the gray scale between black and white, or a combination of those.

Target Market(s)

Drive by visuals

Industry/Entity Type

Real Estate Agent

Colors

Designer to choose only greyscale colors for use in the design.

Requirements
Must have
• My Logo and business name in same/similar font to whats provided, the MF tundra circle logo (small on bottom or corner somewhere), My phone number, and a decent amount of red coloration on the sign.

```html
<!DOCTYPE html>
<html lang="en">
<head>
<meta charset="utf-8">
<title>Brannick Realty – Yard Sign</title>
<link rel="stylesheet" href="https://fonts.googleapis.com/css2?family=Montserrat:wght@800&family=Open+Sans:wght@400;700;800&family=Oswald:wght@700&display=swap">
<style>
  :root {
    --red: #e3141f;
    --ink: #2b2b2b;
    --charcoal: #333333;
    --grey-band: #ececec;
    --backdrop: #d9d9d9;
    --white: #ffffff;
  }
  html, body {
    margin: 0;
    padding: 0;
    width: 1200px;
    height: 1200px;
    overflow: hidden;
    background: var(--backdrop);
  }
  .sign {
    position: absolute;
    left: 170px;
    top: 30px;
    width: 860px;
    height: 1140px;
    overflow: hidden;
    background: linear-gradient(100deg, #dfe6ec 0%, #f3f5f7 45%, var(--white) 100%);
    box-shadow: 0 6px 24px rgba(0,0,0,0.18);
    font-family: "Open Sans", sans-serif;
  }
  .sign-art {
    position: absolute;
    inset: 0;
  }
  .brand {
    position: absolute;
    left: 175px;
    top: 62px;
    display: flex;
    align-items: center;
    gap: 42px;
  }
  .brand-square {
    width: 140px;
    height: 140px;
    background: var(--red);
  }
  .brand-name {
    font-family: "Montserrat", sans-serif;
    font-weight: 800;
    font-size: 70px;
    line-height: 0.98;
    color: var(--ink);
    letter-spacing: 0.5px;
  }
  .agent-name {
    position: absolute;
    left: 0;
    right: 0;
    top: 378px;
    text-align: center;
    font-family: "Oswald", sans-serif;
    font-weight: 700;
    font-size: 118px;
    line-height: 1;
    color: var(--ink);
    letter-spacing: 1px;
  }
  .agent-phone {
    position: absolute;
    left: 0;
    right: 0;
    top: 522px;
    text-align: center;
    font-weight: 700;
    font-size: 48px;
    line-height: 1;
    color: var(--red);
  }
  .phone-rule {
    position: absolute;
    left: 350px;
    top: 584px;
    width: 160px;
    height: 3px;
    background: var(--red);
  }
  .agent-email {
    position: absolute;
    left: 0;
    right: 0;
    top: 592px;
    text-align: center;
    font-weight: 400;
    font-size: 44px;
    color: var(--charcoal);
  }
  .disclaimer {
    position: absolute;
    left: 0;
    right: 0;
    top: 944px;
    text-align: center;
  }
  .disclaimer-line {
    font-weight: 800;
    font-size: 30px;
    line-height: 1.2;
    color: var(--ink);
  }
  .disclaimer-highlight {
    display: inline-block;
    margin-top: 4px;
    padding: 4px 16px;
    background: var(--red);
    color: var(--white);
    font-weight: 800;
    font-size: 30px;
    line-height: 1.2;
  }
  .brokerage {
    position: absolute;
    left: 0;
    right: 0;
    top: 1060px;
    text-align: center;
    color: var(--charcoal);
  }
  .brokerage-name {
    font-weight: 700;
    font-size: 28px;
    line-height: 1;
  }
  .brokerage-sub {
    margin-top: 4px;
    font-weight: 400;
    font-size: 13px;
    letter-spacing: 1px;
    color: #777777;
  }
</style>
</head>
<body>
  <main class="sign">
    <svg class="sign-art" width="860" height="1140" viewBox="0 0 860 1140">
      <defs>
        <linearGradient id="lawnFade" x1="0" y1="0" x2="0" y2="1">
          <stop offset="0" stop-color="#f4f5f5" stop-opacity="0"/>
          <stop offset="0.22" stop-color="#dcd6ca"/>
          <stop offset="0.4" stop-color="#b99f80"/>
          <stop offset="0.52" stop-color="#8c9466"/>
          <stop offset="0.68" stop-color="#78a54a"/>
          <stop offset="1" stop-color="#93c052"/>
        </linearGradient>
      </defs>
      <rect class="scene-fill" role="img" aria-label="Blurred photo of a neighbourhood of homes behind a green lawn" x="0" y="640" width="860" height="420" fill="url(#lawnFade)"/>
      <path class="header-panel" d="M0,0 H860 V210 Q430,460 0,220 Z" fill="#ffffff"/>
      <path class="header-rule-dark" d="M0,200 Q440,458 860,225" fill="none" stroke="#2b2b2b" stroke-width="2.5"/>
      <path class="header-rule-red" d="M0,240 Q430,467 860,195" fill="none" stroke="#e3141f" stroke-width="2.5"/>
      <path class="footer-band" d="M0,995 Q430,778 860,1035 V1140 H0 Z" fill="#ececec"/>
      <path class="footer-rule-red" d="M0,985 Q430,764 860,1020" fill="none" stroke="#e3141f" stroke-width="2.5"/>
      <path class="footer-rule-dark" d="M0,1050 Q420,760 860,1045" fill="none" stroke="#2b2b2b" stroke-width="2.5"/>
    </svg>

    <div class="brand">
      <div class="brand-square"></div>
      <div class="brand-name">BRANNICK<br>REALTY</div>
    </div>

    <h1 class="agent-name" style="margin:0">DANA BRANNICK</h1>
    <div class="agent-phone">907-555-0148</div>
    <div class="phone-rule"></div>
    <div class="agent-email">dana@brannickhomes.com</div>

    <div class="disclaimer">
      <div class="disclaimer-line">EACH OFFICE INDEPENDENTLY</div>
      <div class="disclaimer-highlight">OWNED AND OPERATED</div>
    </div>

    <div class="brokerage">
      <div class="brokerage-name">MF tundra circle</div>
      <div class="brokerage-sub">MARDEN FOSK REALTY</div>
    </div>
  </main>
</body>
</html>
```